Software company specialized in data analytics and professional services

We need a landing page design for our business. It should include our logo design. It should have multiple sections :
- stylish head
- what we do (data analytics software, professional services)
- contact form

Target Market(s)

Companies, B2B

Industry/Entity Type

Data

Number of Pages Required

1 page

Font styles to use
Sans Serif

Requirements
Must have
• Dark theme
Should not have
• Gradients on buttons

```html
<!DOCTYPE html>
<html lang="en">
<head>
<meta charset="utf-8">
<title>Lumora Technology</title>
<link href="https://fonts.googleapis.com/css2?family=Poppins:ital,wght@0,400;0,500;0,600;0,700;1,400&display=swap" rel="stylesheet">
<style>
:root{
  --magenta:#d81b9c;
  --accent:#8fa3ff;
  --bg:#0e1124;
  --band:#151a33;
  --card:#1d2342;
  --card-line:#2b3259;
  --text:#eef0f8;
  --body:#b9bfd6;
  --muted:#8d93ad;
  --star:#f5b400;
  --title-grad:linear-gradient(90deg,#e0259f,#8fa3ff);
}
*{box-sizing:border-box;margin:0;padding:0}
html,body{width:1200px;height:5367px;overflow:hidden}
body{font-family:'Poppins',sans-serif;color:var(--text);background:var(--bg);position:relative}
.abs{position:absolute}
.grad-text{background:var(--title-grad);-webkit-background-clip:text;background-clip:text;color:transparent}
.btn{position:absolute;display:flex;align-items:center;justify-content:center;color:#fff;background:var(--magenta);font-size:18px;font-weight:500}

.header{top:0;left:0;width:1200px;height:150px;background:var(--bg);border-bottom:1px solid var(--card-line)}
.logo{left:96px;top:48px;font-size:44px;font-weight:600;color:var(--magenta);letter-spacing:1px}
.nav{left:468px;top:64px;display:flex;gap:26px;font-size:14px;color:var(--body)}
.nav .active{color:var(--magenta);border-bottom:2px solid var(--accent);padding-bottom:2px}
.nav-cta{left:977px;top:56px;width:141px;height:40px;border:2px solid var(--magenta);color:var(--text);font-size:15px;font-weight:500;display:flex;align-items:center;justify-content:center}

.hero{top:150px;left:0;width:1200px;height:586px;background:linear-gradient(90deg,#12162e 0%,#1a1f3b 50%,#3b3640 75%,#5e5752 100%)}
.hero-title{left:96px;top:338px;font-size:46px;font-weight:500;letter-spacing:1px}
.hero-text{left:98px;top:410px;width:620px;font-size:14.5px;line-height:22px;color:var(--body)}
.hero-btn{left:98px;top:505px;width:160px;height:48px}

.band{left:0;width:1200px}
.soft{background:var(--band)}
.section-title{width:1200px;text-align:center;font-size:40px;font-weight:600;letter-spacing:1px}

.sub-title{font-size:31px;font-weight:500}
.sub-title .dark{color:var(--text)}
.sub-title .pink{color:var(--magenta)}
.para{font-size:17px;line-height:25px;color:var(--body)}

.feature{position:absolute;width:456px;height:100px;background:var(--card);border:1px solid var(--card-line);border-radius:6px;box-shadow:0 3px 10px rgba(0,0,0,.3);display:flex;align-items:center;padding:0 16px}
.feature .ic{width:58px;height:58px;flex:none;margin-right:14px}
.feature h4{font-size:14px;font-weight:500;color:var(--magenta);margin-bottom:6px}
.feature h4 span{color:var(--accent)}
.feature p{font-size:13px;line-height:18px;color:var(--body)}

.photo{border-radius:6px}

.svc{position:absolute;top:2352px;width:324px;height:450px;background:var(--band);border:1px solid var(--card-line);padding:10px}
.svc.raised{background:var(--card);box-shadow:0 8px 20px rgba(0,0,0,.4)}
.svc .img{width:304px;height:200px}
.svc h4{margin:50px 18px 20px;font-size:16px;font-weight:500;color:var(--magenta)}
.svc h4 span{color:var(--accent)}
.svc p{margin:0 18px;font-size:14px;line-height:22px;color:var(--body)}
.svc .more{margin:22px 18px 0;font-size:14px;font-weight:500;color:var(--magenta);display:flex;align-items:center;gap:8px}

.why{position:absolute;top:3185px;width:340px;text-align:center}
.why svg{display:block;margin:0 auto 14px}
.why h4{font-size:17px;font-weight:500;color:var(--magenta);margin-bottom:16px}
.why h4 span{color:var(--accent)}
.why p{font-size:14px;line-height:22px;color:var(--body);padding:0 40px}

.avatar{position:absolute;border-radius:50%}
.arrow{position:absolute;width:42px;height:42px;border-radius:50%;background:var(--magenta);display:flex;align-items:center;justify-content:center}

.field{position:absolute;left:182px;width:833px;background:var(--card);border:1px solid var(--card-line);font-size:16px;color:var(--muted);padding:16px 18px}

.f-col{position:absolute;top:4935px}
.f-col h5{font-size:20px;font-weight:500;color:var(--magenta)}
.f-col h5 span{color:var(--accent)}
.f-col .bar{width:40px;height:3px;background:var(--magenta);margin:12px 0 24px}
.f-col li{list-style:none;font-size:15px;color:var(--body);margin-bottom:10px}
.f-col li::before{content:"›";margin-right:12px;color:var(--body)}
.bottom{top:5250px;height:117px;background:var(--band)}
.social{position:absolute;top:5278px;width:40px;height:40px;border-radius:50%;border:2px solid var(--accent)}
</style>
</head>
<body>

<header class="abs header">
  <div class="abs logo">LUMORA</div>
  <nav class="abs nav">
    <span class="active">HOME</span><span>ABOUT US</span><span>OUR SERVICES</span><span>BLOGS</span><span>TESTIMONIALS</span>
  </nav>
  <div class="abs nav-cta">Contact Us</div>
</header>

<section class="abs hero" role="img" aria-label="Photo of a woman working at a laptop in a bright office"></section>
<h1 class="abs hero-title grad-text">LUMORA TECHNOLOGY</h1>
<p class="abs hero-text">Lorem ipsum dolor sit amet, consectetur adipiscing elit, sed do eiusmod tempor incididunt ut labore et dolore magna aliqua. Quis ipsum suspendisse ultrices viverra maecenas accumsan lacus vel facilisis.</p>
<div class="btn hero-btn">Read More</div>

<section class="abs band soft" style="top:736px;height:1469px"></section>
<h2 class="abs section-title grad-text" style="top:818px">WHAT WE DO</h2>

<h3 class="abs sub-title" style="left:100px;top:950px"><span class="pink">Data Analytics</span> <span class="dark">Software</span></h3>
<p class="abs para" style="left:102px;top:1005px;width:580px">Lorem ipsum dolor sit amet, consectetur adipiscing elit, sed do eiusmod tempor incididunt ut labore et dolore magna aliqua. Quis ipsum suspendisse ultrices gravida.</p>

<div class="feature" style="left:90px;top:1110px">
  <svg class="ic" viewBox="0 0 58 58"><circle cx="29" cy="29" r="27" fill="none" stroke="#6f6a9e" stroke-dasharray="3 3"/><rect x="20" y="20" width="18" height="18" rx="3" fill="none" stroke="#c07be6" stroke-width="2"/></svg>
  <div><h4>UNITED <span>BY DATA</span></h4><p>Our staff works on a contingency fee basis, meaning secure a settlement.</p></div>
</div>
<div class="feature" style="left:90px;top:1222px">
  <svg class="ic" viewBox="0 0 58 58"><circle cx="29" cy="29" r="27" fill="none" stroke="#6f6a9e" stroke-dasharray="3 3"/><rect x="20" y="20" width="18" height="18" rx="3" fill="none" stroke="#c07be6" stroke-width="2"/></svg>
  <div><h4>DATA <span>CULTURE</span></h4><p>Our staff works &nbsp;secure a settlement.</p></div>
</div>
<div class="feature" style="left:90px;top:1335px">
  <svg class="ic" viewBox="0 0 58 58"><circle cx="29" cy="29" r="27" fill="none" stroke="#6f6a9e" stroke-dasharray="3 3"/><rect x="20" y="20" width="18" height="18" rx="3" fill="none" stroke="#c07be6" stroke-width="2"/></svg>
  <div><h4>PRACTICE DATA-<span>DRIVEN BEHAVIORS</span></h4><p>Our staff works on a contingency fee basis, meaning secure a settlement.</p></div>
</div>
<div class="abs photo" style="left:738px;top:912px;width:326px;height:556px;background:linear-gradient(160deg,#c9ccd2,#b09a80 60%,#7d6852)" role="img" aria-label="Photo of a businesswoman presenting a bar chart"></div>

<div class="abs photo" style="left:88px;top:1520px;width:326px;height:556px;background:linear-gradient(180deg,#2c3a30,#1b2219 60%,#0f130f)" role="img" aria-label="Photo of a man holding a laptop showing a hacked warning"></div>
<h3 class="abs sub-title" style="left:478px;top:1567px"><span class="pink">Professional</span> <span class="dark">Services</span></h3>
<p class="abs para" style="left:480px;top:1622px;width:580px">Lorem ipsum dolor sit amet, consectetur adipiscing elit, sed do eiusmod tempor incididunt ut labore et dolore magna aliqua. Quis ipsum suspendisse ultrices gravida.</p>

<div class="feature" style="left:468px;top:1720px">
  <svg class="ic" viewBox="0 0 58 58"><circle cx="29" cy="29" r="27" fill="none" stroke="#6f6a9e" stroke-dasharray="3 3"/><rect x="20" y="20" width="18" height="18" rx="3" fill="none" stroke="#c07be6" stroke-width="2"/></svg>
  <div><h4>VALUE STRATEGIC <span>DATA USE</span></h4><p>Our staff works on a contingency fee basis, meaning secure a settlement.</p></div>
</div>
<div class="feature" style="left:468px;top:1833px">
  <svg class="ic" viewBox="0 0 58 58"><circle cx="29" cy="29" r="27" fill="none" stroke="#6f6a9e" stroke-dasharray="3 3"/><rect x="20" y="20" width="18" height="18" rx="3" fill="none" stroke="#c07be6" stroke-width="2"/></svg>
  <div><h4>WE WIN OR U <span>DONT PAY</span></h4><p>Our staff works &nbsp;secure a settlement.</p></div>
</div>
<div class="feature" style="left:468px;top:1945px">
  <svg class="ic" viewBox="0 0 58 58"><circle cx="29" cy="29" r="27" fill="none" stroke="#6f6a9e" stroke-dasharray="3 3"/><rect x="20" y="20" width="18" height="18" rx="3" fill="none" stroke="#c07be6" stroke-width="2"/></svg>
  <div><h4>ENCOURAGE SHARING <span>&amp; COMMUNITY</span></h4><p>Our staff works on a contingency fee basis, meaning secure a settlement.</p></div>
</div>

<h2 class="abs section-title grad-text" style="top:2268px">OUR SERVICES</h2>
<div class="svc" style="left:104px">
  <div class="img" style="background:linear-gradient(135deg,#5a5944,#857b60 50%,#a39c8d)" role="img" aria-label="Photo of hands using a phone over a laptop"></div>
  <h4>CLOUD <span>SERVICES</span></h4>
  <p>Cloud services provide many ways for business team members to with the technology they need.</p>
</div>
<div class="svc raised" style="left:442px;top:2340px">
  <div class="img" style="background:linear-gradient(135deg,#1c2328,#2d3a40 50%,#141a1d)" role="img" aria-label="Photo of code on a dark screen"></div>
  <h4>BACKUP <span>SOLUTIONS</span></h4>
  <p>Backup solutions protect external hardware or online</p>
  <div class="more">READ <span style="color:var(--accent)">MORE</span>
    <svg width="18" height="18" viewBox="0 0 18 18"><circle cx="9" cy="9" r="7.5" fill="none" stroke="#8fa3ff" stroke-width="1.5"/><path d="M6 9h6M9.5 6.5 12 9l-2.5 2.5" fill="none" stroke="#8fa3ff" stroke-width="1.5"/></svg></div>
</div>
<div class="svc" style="left:778px">
  <div class="img" style="background:linear-gradient(135deg,#d6d6d2,#a9a6a0 50%,#6e6a65)" role="img" aria-label="Photo of a person working at computers in an office"></div>
  <h4>NETWORK <span>SECURITY</span></h4>
  <p>etwork security services help protect a business' network from unauthorized access.</p>
</div>
<div class="btn" style="left:517px;top:2842px;width:173px;height:50px">View More</div>

<section class="abs band soft" style="top:2972px;height:540px"></section>
<h2 class="abs section-title grad-text" style="top:3055px">WHY CHOOSE US</h2>
<div class="why" style="left:106px">
  <svg width="70" height="70" viewBox="0 0 70 70"><circle cx="33" cy="37" r="26" fill="none" stroke="#d81b9c" stroke-width="6"/><circle cx="33" cy="37" r="15" fill="none" stroke="#8fa3ff" stroke-width="5"/><circle cx="33" cy="37" r="5" fill="#d81b9c"/><path d="M33 37 60 10" stroke="#8fa3ff" stroke-width="4"/></svg>
  <h4>EXPE<span>RIENCE</span></h4>
  <p>Our experienced team will assess your eligibility for various rebates for refunds.</p>
</div>
<div class="why" style="left:431px">
  <svg width="70" height="70" viewBox="0 0 70 70"><path d="M6 30 20 18 34 26 48 18 64 30 46 50 34 44 24 50Z" fill="none" stroke="#c07be6" stroke-width="2.5"/><path d="M24 40 34 32 44 40" fill="none" stroke="#8fa3ff" stroke-width="2.5"/></svg>
  <h4>EXPERT <span>ASSESSMENT</span></h4>
  <p>Our experienced team will assess your eligibility for various rebates for refunds.</p>
</div>
<div class="why" style="left:772px">
  <svg width="70" height="70" viewBox="0 0 70 70"><path d="M35 10a24 24 0 0 1 22 14M58 44a24 24 0 0 1-22 16M14 48a24 24 0 0 1 0-26" fill="none" stroke="#d81b9c" stroke-width="4"/><circle cx="35" cy="36" r="11" fill="none" stroke="#8fa3ff" stroke-width="3"/><path d="M24 36h22M35 25v22" stroke="#8fa3ff" stroke-width="2"/></svg>
  <h4>CLAIM <span>PROCESSING</span></h4>
  <p>Our experienced team will assess your eligibility for various rebates for refunds.</p>
</div>

<h2 class="abs section-title grad-text" style="top:3575px">TESTIMONIALS</h2>
<div class="avatar" style="left:278px;top:3702px;width:66px;height:66px;background:#8c8f94" role="img" aria-label="Client portrait"></div>
<div class="avatar" style="left:398px;top:3700px;width:82px;height:82px;background:#d9b98c" role="img" aria-label="Client portrait"></div>
<div class="avatar" style="left:546px;top:3678px;width:112px;height:112px;background:#6d6b66" role="img" aria-label="Client portrait"></div>
<div class="avatar" style="left:724px;top:3700px;width:82px;height:82px;background:#5a4e40" role="img" aria-label="Client portrait"></div>
<div class="avatar" style="left:864px;top:3702px;width:66px;height:66px;background:#d8d4d0" role="img" aria-label="Client portrait"></div>
<div class="arrow" style="left:133px;top:3834px"><svg width="14" height="14" viewBox="0 0 14 14"><path d="M9 2 4 7l5 5" fill="none" stroke="#fff" stroke-width="2.5"/></svg></div>
<div class="arrow" style="left:1033px;top:3834px"><svg width="14" height="14" viewBox="0 0 14 14"><path d="M5 2l5 5-5 5" fill="none" stroke="#fff" stroke-width="2.5"/></svg></div>
<div class="abs" style="left:0;top:3818px;width:1200px;text-align:center">
  <div style="font-size:21px;color:var(--text)">Daniel</div>
  <div style="font-size:17px;font-style:italic;color:var(--magenta);margin-top:2px">Assit <span style="color:var(--accent)">Manager</span></div>
  <div style="font-size:26px;color:var(--star);letter-spacing:2px;line-height:32px">★★★★★</div>
  <p style="font-size:14.5px;line-height:23px;color:var(--body);width:730px;margin:6px auto 0">Lorem ipsum dolor sit amet, consectetur adipiscing elit, sed do eiusmod tempor incididunt ut labore et dolore magna aliqua. Quis ipsum suspendisse ultrices gravida. Risus commodo viverra maecenas accumsan lacus vel facilisis.</p>
</div>

<section class="abs band soft" style="top:4115px;height:735px"></section>
<h2 class="abs section-title grad-text" style="top:4162px">CONTACT US</h2>
<p class="abs" style="left:0;top:4238px;width:1200px;text-align:center;font-size:17px;line-height:28px;color:var(--body)">The Firm is also closed periodically throughout the year to complete training. A sign will be<br>posted meeting or training takes place.</p>
<div class="field" style="top:4345px;height:56px">Full Name :</div>
<div class="field" style="top:4409px;height:56px">E Mail Address :</div>
<div class="field" style="top:4472px;height:56px">Phone Number :</div>
<div class="field" style="top:4537px;height:143px;padding-top:30px">Full Name :</div>
<div class="btn" style="left:493px;top:4707px;width:211px;height:55px;font-size:20px">Send Message</div>

<div class="f-col" style="left:210px">
  <h5>Quick <span>Links</span></h5><div class="bar"></div>
  <ul><li>Home</li><li>About Us</li><li>Our Services</li><li>Our Blogs</li><li>Testimonials</li></ul>
</div>
<div class="f-col" style="left:493px">
  <h5>Customer <span>Services</span></h5><div class="bar"></div>
  <ul><li>Contact us</li><li>Site Map</li><li>Terms and Use</li><li>My Account</li></ul>
</div>
<div class="f-col" style="left:760px">
  <h5>Our <span>Newsletter</span></h5><div class="bar"></div>
  <p style="font-size:15px;line-height:20px;color:var(--body);width:250px">Subscribe our newsletter to get the latest news.</p>
  <div style="width:250px;height:40px;border:1.5px solid #6f6a9e;margin-top:20px;background:var(--card)"></div>
  <div style="width:126px;height:38px;background:var(--magenta);color:#fff;font-size:13px;display:flex;align-items:center;justify-content:center;margin-top:20px">SUBSCRIBE</div>
</div>

<section class="abs band bottom"></section>
<div class="social" style="left:90px"></div>
<div class="social" style="left:142px"></div>
<div class="social" style="left:194px"></div>
<div class="social" style="left:246px"></div>
<p class="abs" style="right:86px;top:5288px;font-size:17px;color:var(--magenta)">All Rights Reserved <span style="color:var(--accent)">@ Copyrights 2023</span></p>

</body>
</html>
```